Job application set/company logo

My resume, profile and project file need to be designed in a common, fresh business design, not too playful and colourful
Potentially a logo for my company called Norvale Consulting needs to be designed in a second step. My company is consulting in digitalization and business transformation.

```html
<!DOCTYPE html>
<html lang="en">
<head>
<meta charset="utf-8">
<title>Marten Hollbrook – Resume</title>
<link href="https://fonts.googleapis.com/css2?family=Poppins:wght@300;400;500;600;700&display=swap" rel="stylesheet">
<style>
:root{
  --ink:#1c1d21;
  --ink-soft:#3a3c42;
  --orange:#f0834a;
  --slate:#6f8e98;
  --mist:#b9d3d8;
  --mist-light:#cfe2e5;
  --mist-deep:#bcd5da;
  --paper:#ffffff;
  --stage:#e9ecee;
  --pill:#e6eff1;
}
*{box-sizing:border-box;margin:0;padding:0}
html,body{width:809px;height:1200px;overflow:hidden}
body{background:var(--stage);font-family:'Poppins',sans-serif;color:var(--ink);position:relative}
ul{list-style:none}
.sheet{position:absolute;left:199px;width:410px;height:580px;background:var(--paper);display:grid;grid-template-columns:174px 1fr;overflow:hidden;box-shadow:0 6px 18px rgba(30,40,50,.18)}
.sheet--front{top:12px}
.sheet--back{top:608px}
.side{display:flex;flex-direction:column}
.portrait{height:170px;background:linear-gradient(160deg,#d9d7d2 0%,#b7b3ab 40%,#6b6e74 70%,#d98658 100%)}
.identity{background:var(--ink);color:#fff;padding:12px 16px 10px 18px;height:168px}
.name{font-size:22px;line-height:1;letter-spacing:.2px}
.name__first{display:block;color:var(--orange);font-weight:400}
.name__last{display:block;font-weight:700;margin-top:1px}
.rule{height:1px;background:linear-gradient(90deg,transparent,#555a62,transparent);margin:10px 0 9px}
.side-title{font-size:10px;font-weight:600;letter-spacing:3px;text-transform:uppercase}
.side-title--light{color:#fff}
.side-title--light span{font-weight:400}
.side-title--orange{color:var(--orange)}
.contact{margin-top:7px}
.contact li{display:flex;align-items:flex-start;gap:8px;font-size:6.3px;line-height:1.3;margin-bottom:5px}
.contact svg{flex:0 0 6px;margin-top:1px}
.qualifications{background:var(--mist);flex:1;padding:11px 12px 8px 14px}
.qualifications .side-title{margin-left:6px;margin-bottom:5px}
.pill{display:inline-block;background:var(--pill);color:var(--ink-soft);font-size:5.6px;font-weight:500;letter-spacing:1.6px;text-transform:uppercase;padding:1px 12px 1px 6px;border-radius:6px;margin:2px 0 5px}
.dots li{position:relative;padding-left:9px;font-size:5.8px;line-height:1.22;margin-bottom:4px}
.dots li::before{content:"";position:absolute;left:1px;top:1.5px;width:4px;height:4px;border:.7px solid currentColor;border-radius:50%;background:radial-gradient(circle,currentColor 0 .8px,transparent 1px)}
.dots--tight li{margin-bottom:2px}
.dots b{font-weight:600}
.main{padding:16px 14px 10px 10px}
.timeline{position:relative;padding-left:14px}
.timeline::before{content:"";position:absolute;left:2px;top:4px;bottom:0;border-left:1px dotted var(--ink-soft)}
.node{position:relative}
.node::before{content:"";position:absolute;left:-14.5px;top:3px;width:5px;height:5px;border-radius:50%;background:var(--ink)}
.main-title{font-size:10.5px;line-height:1.05;font-weight:400;margin-left:-12px}
.main-title em{font-style:normal;color:var(--orange);font-weight:500}
.main-title--spaced{margin-top:12px;margin-bottom:5px}
.topic{font-size:8.6px;line-height:1;color:var(--slate);font-weight:600;margin-top:14px}
.topic span{display:block;font-weight:400}
.topic--role{font-weight:600;margin-top:0}
.topic--role span{display:inline;font-weight:300}
.main .dots{margin-top:6px}
.main .dots li{font-size:6.3px;line-height:1.25;margin-bottom:3px;color:var(--ink-soft)}
.role{margin-top:11px}
.role__head{display:flex;justify-content:space-between;align-items:center;font-size:6.3px;font-weight:600;margin-bottom:2px}
.date{background:var(--ink);color:var(--orange);font-style:italic;font-weight:600;font-size:5.6px;padding:0 5px;line-height:8.5px;white-space:nowrap}
.success{font-size:6.3px;font-weight:600;margin:2px 0 2px 6px}
.role .dots{margin-top:2px}
.role .dots li{margin-bottom:2px}
.role .dots--sub{margin-left:6px;margin-top:0}
/* back sheet */
.education{background:var(--ink);color:#fff;height:244px;padding:16px 16px 0 18px}
.edu{font-size:8px;line-height:1.22;margin-top:8px}
.year{display:inline-block;background:var(--mist);color:var(--ink);font-size:7px;font-weight:500;padding:0 8px;border-radius:6px;margin-top:1px}
.education .rule{margin:18px 0 14px}
.languages{margin-top:8px}
.languages li{font-size:6.5px;margin-bottom:4px}
.languages li span{color:var(--orange);font-weight:500}
.languages li small{font-size:6px}
.activities{background:var(--mist-light);height:123px;padding:22px 16px 0 18px}
.references{background:var(--mist-deep);flex:1;padding:22px 16px 0 18px}
.side-title--dark{color:var(--ink);font-size:10px;letter-spacing:3.6px;margin-bottom:9px}
.plain li{font-size:8px;line-height:1.2;margin-bottom:6px;color:var(--ink-soft)}
.references .plain li{margin-bottom:8px}
.company{font-size:8.6px;font-weight:600;color:var(--slate);margin:20px 0 4px}
.main--back{padding-top:16px}
.main--back .timeline::before{top:0}
.main--back .role{margin-top:14px}
.main--back .role--first{margin-top:0}
</style>
</head>
<body>

<section class="sheet sheet--front" aria-label="Resume page one">
  <aside class="side">
    <div class="portrait" role="img" aria-label="Portrait photo of Marten Hollbrook in a dark suit, arms crossed, office background"></div>
    <div class="identity">
      <h1 class="name"><span class="name__first">MARTEN</span><span class="name__last">HOLLBROOK</span></h1>
      <div class="rule"></div>
      <h2 class="side-title side-title--light">Personal <span>Infos</span></h2>
      <ul class="contact">
        <li><svg width="6" height="6" viewBox="0 0 6 6"><rect x=".3" y="1" width="5.4" height="4" fill="var(--orange)"/><path d="M.3 1 3 3.2 5.7 1" stroke="var(--ink)" stroke-width=".6" fill="none"/></svg>marten.hollbrook@mailpost.net</li>
        <li><svg width="6" height="6" viewBox="0 0 6 6"><path d="M3 .3 5.8 3H5v2.7H3.6V4H2.4v1.7H1V3H.2z" fill="var(--orange)"/></svg>Lindenweg 12<br>50667 Ravensfeld, Germany</li>
        <li><svg width="6" height="6" viewBox="0 0 6 6"><rect x=".4" y="1" width="5.2" height="4.6" fill="var(--orange)"/><rect x=".4" y="1" width="5.2" height="1.2" fill="#c65f2b"/></svg>17.03.1968</li>
        <li><svg width="6" height="6" viewBox="0 0 6 6"><rect x=".4" y=".4" width="5.2" height="5.2" fill="var(--orange)"/></svg>www.profilenet.com/in/martenhollbrook</li>
      </ul>
    </div>
    <div class="qualifications">
      <h2 class="side-title">Qualifications</h2>
      <span class="pill">Core Competencies</span>
      <ul class="dots">
        <li><b>Passionate Digital Transformation</b> Leader with track record of launching and growing business</li>
        <li><b>Entrepreneurial background</b> with network to global innovation hubs</li>
        <li><b>Strong Product &amp; Innovation competence</b> with a clear understanding of market needs</li>
        <li><b>Track record in driving partnerships</b> into highly successful collaborations</li>
      </ul>
      <span class="pill">Accomplishments</span>
      <ul class="dots dots--tight">
        <li>Mentor at Brightforge Launchpad program for start-ups</li>
        <li>Crash Course in Data Science at Westbrook University</li>
        <li>Intro to Blockchain Technology at Alpine Business Institute</li>
        <li>PSM 1, Certified Scrum Master, Agile Guild</li>
        <li>Leadership Excellence Program at Meridian Business School</li>
      </ul>
    </div>
  </aside>

  <main class="main">
    <div class="timeline">
      <h2 class="main-title">PROFILE &amp;<br><em>ACHIEVEMENTS</em></h2>

      <h3 class="topic node">GUIDING ENTREPRENEURIAL<span>INNOVATIONS</span></h3>
      <ul class="dots">
        <li>Define a way forward for Corvantis's Messaging business</li>
        <li>Shape a venture for Elvora in the eMobility segment</li>
        <li>Build a joint venture of Nordtel and Lenscraft for the development of connected smart glasses</li>
      </ul>

      <h3 class="topic node">LEADING GLOBAL PARTNERSHIP<span>NETWORKS</span></h3>
      <ul class="dots">
        <li>Overcome strategic objectives and form an alliance of Quarrion and Corvantis in Messaging</li>
        <li>Position Nordtel as first choice for Pomeris smartphones with a purchase volume of more than 2 billion euro</li>
        <li>Create exclusive advantages for Nordtel customers through partnerships with major innovators like Pomeris and Rivenshop</li>
      </ul>

      <h3 class="topic node">DELIVERY-ORIENTED PRODUCT<span>LEADER</span></h3>
      <ul class="dots">
        <li>Manage the roll out of new GSM-R Units to &gt;5000 vehicles for Railnet AG in logistics and technical integration</li>
        <li>Open the door for IoT business of Veloquence to access European telcos</li>
        <li>Develop a consistent Aurora@home experience and build the corresponding device portfolio supporting DSL, TV, Smart Home</li>
      </ul>

      <h2 class="main-title main-title--spaced">EXPERIENCE <em>(EXEMPLARY)</em></h2>
      <h3 class="topic topic--role node">SENIOR ADVISOR <span>(self-employed)</span></h3>

      <div class="role">
        <div class="role__head"><span>Incubra Corporate Startups</span><span class="date">10/2020 – Present</span></div>
        <ul class="dots">
          <li>Venture building (e.g. with Elvora and NT)</li>
          <li>Derive a product strategy and go to market plan</li>
        </ul>
        <p class="success">Key Success</p>
        <ul class="dots dots--sub"><li>Successful start of Varion, the Elvora eMobility venture</li></ul>
      </div>

      <div class="role">
        <div class="role__head"><span>Veloquence Communications</span><span class="date">08/2021 – Present</span></div>
        <ul class="dots">
          <li>Venture building (e.g. with Elvora and NT)</li>
          <li>Derive a product strategy and go to market plan</li>
        </ul>
        <p class="success">Key Success</p>
        <ul class="dots dots--sub"><li>Growth through new distribution channels via carriers</li></ul>
      </div>

      <div class="role">
        <div class="role__head"><span>Corvantis</span><span class="date">04/2021 – 04/2022</span></div>
        <ul class="dots">
          <li>Evaluation of the global messaging business</li>
          <li>Define a new strategy for messaging in Corvantis</li>
          <li>Implement a new independent business unit for SaaS</li>
        </ul>
        <p class="success">Key Success</p>
        <ul class="dots dots--sub"><li>Successful start of the new business unit</li></ul>
      </div>
    </div>
  </main>
</section>

<section class="sheet sheet--back" aria-label="Resume page two">
  <aside class="side">
    <div class="education">
      <h2 class="side-title side-title--orange">University</h2>
      <p class="edu">Executive Leadership Development Program at Halden Graduate School of Business<br><span class="year">(2016)</span></p>
      <p class="edu">Diploma in Electrical Engineering at Technische Hochschule Arnsberg (THA)<br><span class="year">(1987–1994)</span></p>
      <div class="rule"></div>
      <h2 class="side-title side-title--orange">Languages</h2>
      <ul class="dots languages">
        <li>German <small>(Native)</small></li>
        <li><span>English</span><small>(Full professional proficiency)</small></li>
      </ul>
    </div>
    <div class="activities">
      <h2 class="side-title side-title--dark">Activities</h2>
      <ul class="dots plain">
        <li>Sport: Skiing, Tennis, Hiking, Yoga</li>
        <li>Music: Classical Piano</li>
        <li>Travelling: Europe, Africa, America</li>
      </ul>
    </div>
    <div class="references">
      <h2 class="side-title side-title--dark">References</h2>
      <ul class="dots plain">
        <li>Anselm Brückner, CEO Nordtel</li>
        <li>Jonas Feldkamp, SVP Global Strategic Projects and Marketing Partnerships, Nordtel</li>
        <li>Luc Garnier, formerly CEO Velant Corporation</li>
      </ul>
    </div>
  </aside>

  <main class="main main--back">
    <div class="timeline">
      <div class="role role--first">
        <div class="role__head"><span>Northpoint Consulting</span><span class="date">10/2020 – 12/2022</span></div>
        <ul class="dots"><li>Steering of a group wide exchange of GSM-R equipment</li></ul>
        <p class="success">Key Success</p>
        <ul class="dots dots--sub"><li>Improvement of the mobile connectivity experience for customers of the Railnet AG</li></ul>
      </div>

      <h3 class="company node">NORDTEL AG, RAVENSFELD</h3>
      <div class="role">
        <div class="role__head"><span>Senior Vice President Connected Devices</span><span class="date">08/2011 – 07/2020</span></div>
        <ul class="dots">
          <li>Management of the global partnerships with Pomeris, Quarrion, Kyren</li>
          <li>Board member of Lumio Inc, a JV of NT and Lenscraft AG</li>
          <li>Driving the entire portfolio of devices for the NT group including Wearables, Voice Controlled Devices and Virtual Reality Glasses</li>
        </ul>
        <p class="success">Key Successes</p>
        <ul class="dots dots--sub">
          <li>Managing a turnover of more than 3 billion euros with devices across the Nordtel group</li>
          <li>Development of the first Aurora Voice Speaker</li>
          <li>Foundation of the Lumio joint venture</li>
        </ul>
      </div>
      <div class="role">
        <div class="role__head"><span>Vice President Product<br>Management Mobile</span><span class="date">04/2008 – 07/2011</span></div>
        <ul class="dots">
          <li>Introduction of the international portfolio of mobile phones in Nordtel</li>
          <li>Project lead for key initiatives, e.g. introduction of OpenDroid</li>
        </ul>
        <p class="success">Key Successes</p>
        <ul class="dots dots--sub">
          <li>Successful introduction of the first OpenDroid phone in an exclusive partnership with Quarrion and Velant</li>
          <li>Development of the NT App portfolio for MobiOS and OpenDroid</li>
        </ul>
      </div>

      <h3 class="company node">MOBILNET INTERNATIONAL, RAVENSFELD</h3>
      <div class="role role--first">
        <div class="role__head"><span>Head of Client Integration/ISP Products</span><span class="date">09/1994 – 03/2008</span></div>
        <ul class="dots">
          <li>Conception and development of a branded mobile phone</li>
          <li>Transformation of product management from voice-centric into mobile internet business</li>
        </ul>
      </div>
      <div class="role">
        <div class="role__head"><span>Project Lead Personal Communication<br>Services</span></div>
        <ul class="dots"><li>Project lead of the first FMC product combining fixed and mobile communication on one bill with one device and one service</li></ul>
      </div>
      <div class="role">
        <div class="role__head"><span>Project Engineering</span></div>
        <ul class="dots">
          <li>Project lead “Short Message Service Center”</li>
          <li>Voice quality assurance: Design of a new measurement system and implementation in C++</li>
          <li>Audits of system technology suppliers</li>
        </ul>
      </div>
    </div>
  </main>
</section>

</body>
</html>
```